Business card for auto dealership

Looking for a clean modern design.
Would like attached logo incorporated

Industry/Entity Type

Car dealership

Contact Information for Business Card

Name, website, phone, cell, fax, email

```html
<!DOCTYPE html>
<html lang="en">
<head>
<meta charset="utf-8">
<title>Halvorsen Truck &amp; Auto Sales — Business Card</title>
<link href="https://fonts.googleapis.com/css2?family=Open+Sans:wght@400;700&family=Pacifico&display=swap" rel="stylesheet">
<style>
  :root {
    --backdrop: #2f3132;
    --card-dark: #151515;
    --card-light: #ffffff;
    --ink: #111111;
    --logo-on-dark: #b9b9b9;
    --rule: #222222;
  }
  * { box-sizing: border-box; margin: 0; padding: 0; }
  html, body { width: 1200px; height: 1122px; overflow: hidden; }
  body {
    background: var(--backdrop);
    font-family: "Open Sans", sans-serif;
    display: flex;
    flex-direction: column;
    align-items: center;
    justify-content: center;
    gap: 50px;
  }
  .card {
    width: 880px;
    height: 503px;
    border-radius: 28px;
    position: relative;
  }
  .card--front {
    background: var(--card-dark);
    display: flex;
    align-items: center;
    justify-content: center;
  }
  .card--back {
    background: var(--card-light);
    color: var(--ink);
    display: flex;
    align-items: center;
  }
  .wordmark {
    font-family: "Open Sans", sans-serif;
    font-weight: 700;
    text-align: center;
    line-height: 1.05;
    display: flex;
    align-items: center;
    gap: 16px;
  }
  .wordmark__dot {
    width: 22px; height: 22px; border-radius: 50%;
    background: currentColor; flex: none;
  }
  .wordmark__name { font-size: 70px; letter-spacing: 1px; }
  .wordmark__tag { font-size: 22px; letter-spacing: 3px; text-transform: uppercase; display: block; }
  .card--front .wordmark { color: var(--logo-on-dark); }
  .card--back .wordmark { color: var(--ink); }
  .card--back .wordmark__name { font-size: 48px; }
  .card--back .wordmark__tag { font-size: 15px; letter-spacing: 2px; }
  .card__brand {
    width: 470px;
    display: flex;
    justify-content: center;
  }
  .card__divider {
    width: 2px;
    height: 270px;
    background: var(--rule);
  }
  .card__details { padding-left: 40px; }
  .holder-name {
    font-family: "Pacifico", cursive;
    font-size: 34px;
    margin-bottom: 14px;
  }
  .contact-list { list-style: none; }
  .contact-list li {
    display: flex;
    align-items: center;
    gap: 14px;
    font-size: 19px;
    line-height: 31px;
  }
  .contact-list svg { width: 16px; height: 16px; flex: none; fill: var(--ink); }
</style>
</head>
<body>
  <section class="card card--front">
    <div class="wordmark">
      <span class="wordmark__dot"></span>
      <span>
        <span class="wordmark__name">Halvorsen</span>
        <span class="wordmark__tag">Truck &amp; Auto Sales</span>
      </span>
    </div>
  </section>

  <section class="card card--back">
    <div class="card__brand">
      <div class="wordmark">
        <span class="wordmark__dot"></span>
        <span>
          <span class="wordmark__name">Halvorsen</span>
          <span class="wordmark__tag">Truck &amp; Auto Sales</span>
        </span>
      </div>
    </div>
    <div class="card__divider"></div>
    <div class="card__details">
      <p class="holder-name">Dana Halvorsen</p>
      <ul class="contact-list">
        <li><svg viewBox="0 0 16 16" aria-hidden="true"><path d="M3 1l3 3-1.5 2a9 9 0 0 0 5.5 5.5L12 10l3 3-2 2C7 15 1 9 1 3z"/></svg>555-014-2011</li>
        <li><svg viewBox="0 0 16 16" aria-hidden="true"><path d="M4 0h8a1 1 0 0 1 1 1v14a1 1 0 0 1-1 1H4a1 1 0 0 1-1-1V1a1 1 0 0 1 1-1zm1 2v10h6V2zm3 11a1 1 0 1 0 0 2 1 1 0 0 0 0-2z"/></svg>555-014-7140</li>
        <li><svg viewBox="0 0 16 16" aria-hidden="true"><path d="M4 0h8v4H4zM1 5h14a1 1 0 0 1 1 1v6h-3v4H3v-4H0V6a1 1 0 0 1 1-1zm4 6v3h6v-3z"/></svg>555-014-3774</li>
        <li><svg viewBox="0 0 16 16" aria-hidden="true"><path d="M0 3h16v10H0zm1.5 1.2L8 9l6.5-4.8V4h-13z"/></svg>dana@halvorsenauto.com</li>
        <li><svg viewBox="0 0 16 16" aria-hidden="true"><path d="M8 0a8 8 0 1 0 0 16A8 8 0 0 0 8 0zm0 1.5c.9 0 2 2 2.3 5H5.7C6 3.5 7.1 1.5 8 1.5zM5.7 8h4.6c-.3 3-1.4 5-2.3 5s-2-2-2.3-5zM1.6 8h2.6c.1 1.9.5 3.6 1.2 4.7A6.5 6.5 0 0 1 1.6 8zm10.2 0h2.6a6.5 6.5 0 0 1-3.8 4.7c.7-1.1 1.1-2.8 1.2-4.7zM5.4 3.3C4.7 4.4 4.3 5 4.2 6.5H1.6a6.5 6.5 0 0 1 3.8-3.2zm5.2 0a6.5 6.5 0 0 1 3.8 3.2h-2.6c-.1-1.5-.5-2.1-1.2-3.2z"/></svg>Halvorsenauto.com</li>
      </ul>
    </div>
  </section>
</body>
</html>
```